CD Cover Design Project

Don't have a huge brief or visual idea of exactly what i want, but here are the details:

Band Name: The Brinewhistles
Title: Most of Where We Ought to Go
Genre: indie rock - think Carried On Lanterns, Drubb, Tarvy, The Plonts, etc)

Definitely want the name and title on the cover. It could be more photography based or design based. A little more abstract. Totally open. Brinewhistles chew up everything they see... One thought was an eaten, old beat up guitar...maybe too cliche.

Album covers i love: Allwhiles, Marble Sleeping, Sidestep the Pebbles, Dusty Ladders, Make me Drift

Happy to send music or give feedback on concepts prior to working on them...not sure of the rules...whatever is within them.

```html
<!DOCTYPE html>
<html lang="en">
<head>
<meta charset="utf-8">
<title>The Brinewhistles — Most of Where We Ought to Go</title>
<link rel="stylesheet" href="https://fonts.googleapis.com/css2?family=Bebas+Neue&display=swap">
<style>
  :root {
    --door-green: #1f3d23;
    --door-green-deep: #0e1c10;
    --plaster-tan: #a88a68;
    --plaster-light: #b99b78;
    --ink: #0d0d0b;
  }
  html, body {
    margin: 0;
    padding: 0;
    width: 1200px;
    height: 799px;
    overflow: hidden;
    background: var(--door-green-deep);
  }
  .cover {
    position: relative;
    width: 1200px;
    height: 799px;
    overflow: hidden;
  }
  .cover-photo {
    position: absolute;
    inset: 0;
    width: 1200px;
    height: 799px;
  }
  .cover-type {
    position: absolute;
    left: 30px;
    width: 1200px;
    margin: 0;
    text-align: center;
    color: var(--ink);
    font-family: "Bebas Neue", "Arial Narrow", sans-serif;
    font-weight: 400;
    line-height: 1;
    white-space: nowrap;
  }
  .band-name {
    top: 296px;
    font-size: 104px;
    letter-spacing: 3px;
  }
  .album-title {
    top: 452px;
    font-size: 64px;
    letter-spacing: 4px;
  }
</style>
</head>
<body>
  <main class="cover">
    <svg class="cover-photo" viewBox="0 0 1200 799" role="img"
         aria-label="Photograph of a weathered dark green painted door with a large patch of bare tan plaster in the centre and an old keyhole plate at lower left">
      <defs>
        <radialGradient id="door-paint" cx="0.5" cy="0.5" r="0.75">
          <stop offset="0" stop-color="var(--door-green)"/>
          <stop offset="1" stop-color="var(--door-green-deep)"/>
        </radialGradient>
        <radialGradient id="plaster-patch" cx="0.5" cy="0.5" r="0.5">
          <stop offset="0" stop-color="var(--plaster-light)"/>
          <stop offset="1" stop-color="var(--plaster-tan)"/>
        </radialGradient>
        <filter id="soft-edge" x="-10%" y="-10%" width="120%" height="120%">
          <feGaussianBlur stdDeviation="5"/>
        </filter>
      </defs>
      <rect width="1200" height="799" fill="url(#door-paint)"/>
      <ellipse cx="630" cy="420" rx="475" ry="310" fill="url(#plaster-patch)" filter="url(#soft-edge)"/>
    </svg>
    <h1 class="cover-type band-name">The Brinewhistles</h1>
    <h2 class="cover-type album-title">Most of Where We Ought to Go</h2>
  </main>
</body>
</html>
```